Ad design for a macarons brand

We are a dessert brand with one product line: macarons. Our products delight. Every bite is a dream!

We are launching a new product and would like to lunch a small tactical campaign for the product to boost sales.

The new macron is mango ganache and the middle a mix of sour mango and yuzu (https://www.plumvarell.com/about-the-fruit-584302).

Here are some images we took of the new macaron
https://www.fennlocker.com/sh/qrtwpzhkvbmls/AAFJtRWD-nxPlkhQZ7CeW4DLp?dl=0

I attach the brand guideline document.

Required sizes

1080 x 1350
1080 x 1920

```html
<!DOCTYPE html>
<html lang="en">
<head>
<meta charset="UTF-8">
<title>Mirel – Mango Ganache Macaron</title>
<link rel="stylesheet" href="https://fonts.googleapis.com/css2?family=DM+Serif+Display&family=Poppins:wght@400&display=swap">
<style>
  :root {
    --olive: #959a00;
    --sun-top: #f7b62e;
    --sun-bottom: #eda00f;
    --logo-text: #f2b431;
    --mango-light: #f0b24a;
    --mango-deep: #d98a2c;
  }
  * { margin: 0; padding: 0; box-sizing: border-box; }
  html, body {
    width: 960px;
    height: 1200px;
    overflow: hidden;
    background: var(--olive);
  }
  .ad {
    position: relative;
    width: 960px;
    height: 1200px;
    background: var(--olive);
  }
  .ad__field {
    position: absolute;
    left: 25px;
    top: 25px;
    width: 910px;
    height: 1150px;
    background: linear-gradient(180deg, var(--sun-top) 0%, var(--sun-bottom) 100%);
    overflow: hidden;
  }
  .site-url {
    position: absolute;
    top: 25px;
    left: 0;
    width: 100%;
    text-align: center;
    font-family: "Poppins", sans-serif;
    font-size: 20px;
    line-height: 28px;
    color: var(--olive);
  }
  .brand-mark {
    position: absolute;
    left: 342px;
    top: 124px;
    width: 226px;
    height: 113px;
    background: var(--olive);
    display: flex;
    align-items: center;
    justify-content: center;
    font-family: "Poppins", sans-serif;
    font-size: 42px;
    letter-spacing: 2px;
    color: var(--logo-text);
  }
  .headline {
    position: absolute;
    top: 292px;
    left: 0;
    width: 100%;
    text-align: center;
    font-family: "DM Serif Display", serif;
    font-weight: 400;
    font-size: 100px;
    line-height: 98px;
    letter-spacing: -1px;
    color: var(--olive);
  }
  .subline {
    position: absolute;
    top: 525px;
    left: 0;
    width: 100%;
    text-align: center;
    font-family: "Poppins", sans-serif;
    font-size: 35.5px;
    line-height: 46px;
    color: var(--olive);
  }
  .product-panel {
    position: absolute;
    left: 221px;
    top: 765px;
    width: 484px;
    height: 385px;
    background: var(--olive);
  }
  .product-photo {
    position: absolute;
    left: 181px;
    top: 797px;
    width: 569px;
    height: 353px;
    border-radius: 120px 120px 0 0;
    background: radial-gradient(ellipse at 50% 40%, var(--mango-light) 0%, var(--mango-deep) 100%);
  }
</style>
</head>
<body>
<main class="ad">
  <div class="ad__field">
    <p class="site-url">www.mirelbakery.com</p>

    <div class="brand-mark">MIREL</div>

    <h1 class="headline">Every bite’s<br>a dream</h1>
    <p class="subline">New Mango ganache flavor</p>

    <div class="product-panel"></div>

    <div class="product-photo" role="img" aria-label="A pile of mango ganache macarons with blushed orange and green shells and yellow filling"></div>
  </div>
</main>
</body>
</html>
```